Wildlife photographer Website

The website is to be a "resume" of pictures and awards won by Nora. Lean heavy to outdoor wildlife.
She will post articles and have ability to interact with fans.

I will add some of her pictures tonight,

Target Market(s)

Terrain Chronicle .....anyone looking to hire a wildlife photographer.

Industry/Entity Type

Professional Photography

Contact Information for Business Card

Nora Pelham
4817 Quiet Harbor Lane
Columbia MD 38512
518-264-8391
Nora@BrushNora.com

Coding

Coded - Design and coding required

Number of Pages Required

5+ page

Requirements
Must have
• New Logo
Nice to have
• Nature, and eye catching graphics

```html
<!DOCTYPE html>
<html lang="en">
<head>
<meta charset="utf-8">
<title>Nora Pelham – Wildlife Photographer</title>
<link rel="stylesheet" href="https://fonts.googleapis.com/css2?family=Poppins:wght@300;400&family=Roboto+Condensed:wght@400;700&family=Mulish:wght@400;700&display=swap">
<style>
:root{
  --yellow:#fcd62a;
  --ink:#1d1d1d;
  --text:#333333;
  --muted:#555555;
  --gray-band:#e8e9ea;
  --footer:#333333;
  --footer-deep:#262626;
  --white:#ffffff;
  --line:#d8d8d8;
}
*{box-sizing:border-box;margin:0;padding:0}
html,body{width:1200px;height:4345px;overflow:hidden}
body{background:var(--white);color:var(--text);font-family:"Mulish",sans-serif;position:relative}
.section{position:absolute;left:0;width:1200px}
.abs{position:absolute}
.btn{position:absolute;background:var(--yellow);color:var(--ink);font-family:"Roboto Condensed",sans-serif;font-size:20px;display:flex;align-items:center;justify-content:center;border-radius:2px}
.heading{font-family:"Poppins",sans-serif;font-weight:400;color:var(--ink)}
.body-copy{font-size:13.5px;line-height:24.5px;color:var(--text)}
.photo{position:absolute}

/* header */
.site-header{top:0;height:101px;background:var(--white)}
.brand-mark{left:160px;top:15px;width:77px;height:77px;border-radius:50%;background:var(--ink)}
.brand-name{left:246px;top:14px;font-family:"Poppins",sans-serif;font-size:37px;line-height:44px;color:var(--ink)}
.brand-tag{left:247px;top:55px;font-family:"Roboto Condensed",sans-serif;font-size:21px;color:var(--ink)}
.nav-link{top:42px;font-family:"Roboto Condensed",sans-serif;font-size:18px;color:var(--ink)}
.nav-hire{left:915px;top:32px;width:123px;height:44px;font-size:22px}

/* hero */
.hero{top:101px;height:503px;background:linear-gradient(100deg,#2a3325 0%,#3d4432 40%,#4a3a28 65%,#7a4a25 78%,#3b3424 100%)}
.hero-bar{left:160px;top:120px;width:7px;height:263px;background:var(--yellow)}
.hero-kicker{left:197px;top:170px;font-family:"Poppins",sans-serif;font-weight:300;font-size:22px;color:var(--white)}
.hero-title{left:197px;top:200px;font-family:"Poppins",sans-serif;font-weight:300;font-size:39px;color:var(--white)}
.hero-by{left:197px;top:248px;font-family:"Poppins",sans-serif;font-weight:300;font-size:22px;color:var(--white)}
.hero-hire{left:197px;top:289px;width:124px;height:44px;font-size:21px}

/* about */
.about{top:604px;height:637px;background:linear-gradient(120deg,#f6e3d3 0%,#f1ddcc 40%,#ddd2c8 70%,#f3dccb 100%)}
.about-frame{left:145px;top:127px;width:375px;height:395px;border:2px solid var(--yellow)}
.about-photo{left:159px;top:115px;width:376px;height:395px;background:linear-gradient(160deg,#394536,#4c6470 45%,#2d8aa0 70%,#6b5545)}
.about-title{left:562px;top:186px;font-size:27px;color:#333}
.about-text{left:562px;top:224px;width:470px;color:#555}
.about-btn{left:562px;top:405px;width:186px;height:44px;font-size:19px}

/* featured intro */
.featured-intro{top:1241px;height:244px}
.featured-title{left:0;width:1208px;top:72px;text-align:center;font-size:31px}
.featured-lead{left:199px;top:124px;width:771px;text-align:center;font-size:13.3px;line-height:24.5px}
.featured-lead b{font-weight:700;color:var(--ink)}

/* projects */
.project{height:578px}
.project.band{background:var(--gray-band)}
.project-title{font-size:26px;line-height:32px}
.project-text{width:268px}
.project-btn{width:123px;height:44px;font-size:19px}
.p1{top:1485px}
.p2{top:2063px;background:var(--white)}
.p3{top:2641px}

/* articles */
.articles{top:3219px;height:541px}
.articles-title{left:0;width:1200px;top:56px;text-align:center;font-size:26px}
.article{position:absolute;left:162px;width:403px;height:58px;border-bottom:1px solid var(--line)}
.article-date{position:absolute;left:0;top:0;font-size:15px;color:var(--ink)}
.article-teaser{position:absolute;left:0;top:27px;font-size:13.3px;color:var(--text)}
.article-go{position:absolute;right:0;top:23px;width:18px;height:18px}
.articles-btn{left:162px;top:408px;width:104px;height:44px;font-size:19px}
.articles-photo{left:614px;top:123px;width:424px;height:329px;background:linear-gradient(180deg,#4f6b46 0%,#8c6a4e 35%,#b98467 60%,#8a5a44 100%)}

/* footer */
.site-footer{top:3760px;height:527px;background:var(--footer);color:var(--white)}
.footer-title{font-family:"Poppins",sans-serif;font-size:25px;color:var(--white);top:88px}
.footer-rule{top:135px;width:54px;height:3px;background:var(--yellow)}
.footer-intro{left:164px;top:180px;width:400px;font-size:13.3px;line-height:24.5px}
.contact-label{left:164px;font-size:14px;font-weight:700;color:var(--yellow)}
.contact-value{left:246px;font-size:14px;line-height:22px}
.field{position:absolute;border-bottom:1px solid #6b6b6b;font-size:13.3px;color:#e6e6e6;padding-bottom:8px}
.submit{left:613px;top:402px;width:132px;height:44px;font-family:"Mulish",sans-serif;font-weight:700;font-size:13px;letter-spacing:.3px}
.copyright-bar{top:4287px;height:58px;background:var(--footer-deep)}
.copyright{left:160px;top:20px;font-size:12.5px;color:#e6e6e6}
.social{top:17px;width:25px;height:25px}
</style>
</head>
<body>

<header class="section site-header">
  <div class="abs brand-mark"></div>
  <div class="abs brand-name">Nora Pelham</div>
  <div class="abs brand-tag">Wildlife Photographer</div>
  <nav>
    <span class="abs nav-link" style="left:621px">About Me</span>
    <span class="abs nav-link" style="left:729px">My Gallery</span>
    <span class="abs nav-link" style="left:842px">Articles</span>
    <span class="btn nav-hire">Hire Me</span>
  </nav>
</header>

<section class="section hero" role="img" aria-label="Red fox sitting among dark bamboo stems and forest floor">
  <div class="abs hero-bar"></div>
  <div class="abs hero-kicker">Welcome to</div>
  <h1 class="abs hero-title">Wildlife Photography</h1>
  <div class="abs hero-by">By Nora Pelham</div>
  <span class="btn hero-hire">Hire Me</span>
</section>

<section class="section about" role="img" aria-label="Faded background of a photographer lying on the ground aiming a camera">
  <div class="abs about-frame"></div>
  <div class="photo about-photo" role="img" aria-label="Portrait of Nora in a beanie and vest beside a river"></div>
  <h2 class="abs heading about-title">About Nora Pelham</h2>
  <p class="abs body-copy about-text">Lorem ipsum dolor sit amet, consectetuer adipiscing elit, sed dianonummy nibh euismod tincidunt ut laoreet dlore magna aliquam erat volutpat. Ut wisifd fenim ad minim veniam, quis nostrud exerci tation ullamcorper suscipit lobortis nisl ut aliquip ex ea commodo consequat duis. Lorem ipsum dolor sit amet, consectetuer adipiscing elit, sed diam nonummy nibh euismod tincidunt ut laoreet dlore magna aliquam erat volutpat. Ut wisifd fenim ad minim veniam, quis nostrud exerci tation ullamcorper suscipit.</p>
  <span class="btn about-btn">Read More About Me</span>
</section>

<section class="section featured-intro">
  <h2 class="abs heading featured-title">Featured Photography Projects</h2>
  <p class="abs body-copy featured-lead"><b>I have listed my 3 recents project or visited place below</b> lorem ipsum dolor sit amet, consectetuer adipiscing elit, sed diam nonummy nibh euismod tincidunt ut laoreet dolore magna aliquam erat volutpat. Ut wisi enim ad minim veniam, quis nostrud exerci tation ullamcorper suscipit lobortis nisl ut aliquip ex ea commodo consequat. Duis autem vel eum iriure dolor.</p>
</section>

<section class="section project band p1">
  <div class="photo" style="left:162px;top:74px;width:287px;height:206px;background:linear-gradient(180deg,#8f8a7e,#c9b79c 60%,#a89576)" role="img" aria-label="Sandpiper standing on wet sand"></div>
  <div class="photo" style="left:459px;top:74px;width:287px;height:206px;background:linear-gradient(180deg,#3f5660,#5b7480 60%,#2e434b)" role="img" aria-label="Long-tailed duck swimming on dark water"></div>
  <div class="photo" style="left:162px;top:297px;width:287px;height:206px;background:linear-gradient(180deg,#7d8a91,#9aa3a0 55%,#a7823f)" role="img" aria-label="Flock of small birds flying over golden grass"></div>
  <div class="photo" style="left:459px;top:298px;width:287px;height:205px;background:linear-gradient(180deg,#31383a,#7a93a6 50%,#3b3a33)" role="img" aria-label="Blue heron in flight"></div>
  <h3 class="abs heading project-title" style="left:768px;top:150px">Lorem Ispum</h3>
  <p class="abs body-copy project-text" style="left:770px;top:193px">Lorem ipsum dolor sit amet, consectetuer adipiscing elit, sed diam nonummy nibh euismod tincidunt ut laoreet dlore magna aliquam erat volutpat. Ut wisifd fenim ad minim veniam, quis nostrud exerci tation ullamcorper suscipit lobortis nisl ut aliquip ex ea commodo consequat duis.</p>
  <span class="btn project-btn" style="left:770px;top:378px">View Gallery</span>
</section>

<section class="section project p2">
  <h3 class="abs heading project-title" style="left:160px;top:152px">Lorem Ispum</h3>
  <p class="abs body-copy project-text" style="left:162px;top:195px">Lorem ipsum dolor sit amet, consectetuer adipiscing elit, sed diam nonummy nibh euismod tincidunt ut laoreet dlore magna aliquam erat volutpat. Ut wisifd fenim ad minim veniam, quis nostrud exerci tation ullamcorper suscipit lobortis nisl ut aliquip ex ea commodo consequat duis.</p>
  <span class="btn project-btn" style="left:162px;top:374px">View Gallery</span>
  <div class="photo" style="left:456px;top:75px;width:285px;height:205px;background:linear-gradient(180deg,#5d6f86,#e0a545 45%,#6a5a3e 75%,#4a4438)" role="img" aria-label="Sunset sky over a dirt road through fields"></div>
  <div class="photo" style="left:753px;top:75px;width:285px;height:205px;background:linear-gradient(180deg,#b6c2c2,#6f5a45 50%,#a6aca6)" role="img" aria-label="Duck stretching its wings in the water"></div>
  <div class="photo" style="left:456px;top:297px;width:285px;height:205px;background:linear-gradient(180deg,#9a6a30,#5a3c22 55%,#b07b3a)" role="img" aria-label="Otter swimming in amber water"></div>
  <div class="photo" style="left:753px;top:297px;width:285px;height:205px;background:linear-gradient(180deg,#4d5a5e,#b89a62 55%,#6b6a5c)" role="img" aria-label="Waves breaking in golden light"></div>
</section>

<section class="section project band p3">
  <div class="photo" style="left:162px;top:75px;width:287px;height:206px;background:linear-gradient(180deg,#2f3a2a,#8a5230 55%,#3c3526)" role="img" aria-label="Red fox sitting in the forest"></div>
  <div class="photo" style="left:459px;top:75px;width:287px;height:206px;background:linear-gradient(180deg,#2e3a52,#8a6a4a 50%,#c7cfdc)" role="img" aria-label="Rabbit leaping over snow"></div>
  <div class="photo" style="left:162px;top:298px;width:287px;height:205px;background:linear-gradient(180deg,#dfe4ec,#b9a284 55%,#e9ecf1)" role="img" aria-label="Female cardinal perched on snow"></div>
  <div class="photo" style="left:459px;top:298px;width:287px;height:205px;background:linear-gradient(180deg,#9c9788,#c7c0b0 50%,#7d7a6e)" role="img" aria-label="Hummingbird hovering near a rock"></div>
  <h3 class="abs heading project-title" style="left:768px;top:133px">Remote &amp; Camera<br>Trap Photography</h3>
  <p class="abs body-copy project-text" style="left:770px;top:203px">Lorem ipsum dolor sit amet, consectetuer adipiscing elit, sed diam nonummy nibh euismod tincidunt ut laoreet dlore magna aliquam erat volutpat. Ut wisifd fenim ad minim veniam, quis nostrud exerci tation ullamcorper suscipit lobortis nisl ut aliquip ex ea commodo consequat duis.</p>
  <span class="btn project-btn" style="left:770px;top:394px">View Gallery</span>
</section>

<section class="section articles">
  <h2 class="abs heading articles-title">Recent Articles</h2>
  <div class="article" style="top:120px"><span class="article-date">Mar, 03 2021</span><span class="article-teaser">Lorem ipsum dolor sit amet, consectetuer adipiscing sed</span><svg class="article-go" viewBox="0 0 18 18"><circle cx="9" cy="9" r="7.5" fill="none" stroke="#fcd62a" stroke-width="1.5"/><path d="M7.5 5.5 11 9l-3.5 3.5" fill="none" stroke="#fcd62a" stroke-width="1.5"/></svg></div>
  <div class="article" style="top:194px"><span class="article-date">Mar, 05 2021</span><span class="article-teaser">Lorem ipsum dolor sit amet, consectetuer adipiscing sed</span><svg class="article-go" viewBox="0 0 18 18"><circle cx="9" cy="9" r="7.5" fill="none" stroke="#fcd62a" stroke-width="1.5"/><path d="M7.5 5.5 11 9l-3.5 3.5" fill="none" stroke="#fcd62a" stroke-width="1.5"/></svg></div>
  <div class="article" style="top:268px"><span class="article-date">Mar, 08 2021</span><span class="article-teaser">Lorem ipsum dolor sit amet, consectetuer adipiscing sed</span><svg class="article-go" viewBox="0 0 18 18"><circle cx="9" cy="9" r="7.5" fill="none" stroke="#fcd62a" stroke-width="1.5"/><path d="M7.5 5.5 11 9l-3.5 3.5" fill="none" stroke="#fcd62a" stroke-width="1.5"/></svg></div>
  <div class="article" style="top:339px;border-bottom:none"><span class="article-date">Mar, 08 2021</span><span class="article-teaser">Lorem ipsum dolor sit amet, consectetuer adipiscing sed</span><svg class="article-go" viewBox="0 0 18 18"><circle cx="9" cy="9" r="7.5" fill="none" stroke="#fcd62a" stroke-width="1.5"/><path d="M7.5 5.5 11 9l-3.5 3.5" fill="none" stroke="#fcd62a" stroke-width="1.5"/></svg></div>
  <span class="btn articles-btn">View More</span>
  <div class="photo articles-photo" role="img" aria-label="Nora hiking with trekking poles on a rocky trail among pine trees"></div>
</section>

<footer class="section site-footer">
  <h2 class="abs footer-title" style="left:164px">Contact Me</h2>
  <div class="abs footer-rule" style="left:164px"></div>
  <p class="abs footer-intro">Ut wisi enim ad minim veniam, quis nostrud exerci tation ullamcorper suscipit lobortis nisl ut aliquip.</p>
  <span class="abs contact-label" style="top:256px">ADDRESS:</span>
  <span class="abs contact-value" style="top:254px">4817 Quiet Harbor Lane<br>Columbia MD 38512</span>
  <span class="abs contact-label" style="top:324px">PHONE:</span>
  <span class="abs contact-value" style="top:322px">518-264-8391</span>
  <span class="abs contact-label" style="top:370px">EMAIL:</span>
  <span class="abs contact-value" style="top:368px">Nora@BrushNora.com</span>

  <h2 class="abs footer-title" style="left:611px">Send Me A Message!</h2>
  <div class="abs footer-rule" style="left:611px"></div>
  <div class="field" style="left:611px;top:181px;width:205px">First Name</div>
  <div class="field" style="left:835px;top:181px;width:205px">Last Name</div>
  <div class="field" style="left:611px;top:238px;width:205px">Phone</div>
  <div class="field" style="left:835px;top:238px;width:205px">Email</div>
  <div class="field" style="left:611px;top:296px;width:429px;height:62px">Message</div>
  <span class="btn submit">SUBMIT NOW</span>
</footer>

<div class="section copyright-bar">
  <span class="abs copyright">Copyright © 2021 NORA PELHAM. All Rights Reserved.</span>
  <span class="abs social" style="left:916px;background:#3b5a9a" aria-label="Social profile"></span>
  <span class="abs social" style="left:948px;background:#d9345a" aria-label="Social profile"></span>
  <span class="abs social" style="left:981px;background:#3fa6e0" aria-label="Social profile"></span>
  <span class="abs social" style="left:1013px;background:#e32020" aria-label="Social profile"></span>
</div>

</body>
</html>
```